Diesel Trailer Manufacturer Website Design

We are working with a Trailer Manufacturer in Texas. They provide custom-made trailers for diesel trucks throughout the US.
Some sites to use for content/competitors:
www.birchhaulers.com
https://velmotrailers.com
http://www.dunhollowcustomtrailers.com/
https://www.pellingtrailer.com
https://www.roadwren.com
Thank you for taking the time to consider designing a website for us. We are web developers based in Stockton, CA, USA. Most of our projects go through the same process. Understanding this process may help you win a project with us. We custom-code all of our websites in-house. We don’t have any requirements as to what tools you use for your design, but we ask that you follow these guidelines.
IMAGES:
If you use any images or icons in the design, we ask that you have a link to the asset so we can purchase the image/icon. Most of the designs we submit do not have the customer’s images on them unless they have some great images. Be creative; show us the feeling you are trying to portray with your image choices. Use any royalty-free site you choose. We subscribe to Quillor and mainly use their images, but we can purchase images outside of Quillor. PLEASE NOTE: we will not submit designs to clients with watermarks on the images.
FONTS:
We ask that you identify the fonts you’re using in the design. This can be done in a message if you want. We typically use Fennix Fonts and Quillor Fonts.
CONTENT:
We're always open to different content and ideas. We often submit designs with stock images so the client can see our vision. We typically take pictures after the website launch to use their images with our vision. Lorem Ipsum is fine for paragraphs, but we ask that you make the Headers with correct English. We want to be able to show the vision and identify the sections of the website.
INSPIRATION:
We typically add a couple of links in the brief of websites we like to help you get started in your design.
REVISIONS:
We do not often ask for revisions of the designs unless we see something in the design that may not appeal to the client. If there are slight changes that we want to make, we do that in the development process.
FEEDBACK:
We rarely give feedback on designs during the design process. We are working on many website projects and do not have the time to provide feedback. We usually respond if your request is well thought out and asks specific questions, but a note asking “feedback, please” usually goes unanswered.
1 page

```html
<!DOCTYPE html>
<html lang="en">
<head>
<meta charset="utf-8">
<title>Steelbrand — Quality Trailer Manufacturer in Texas</title>
<link href="https://fonts.googleapis.com/css2?family=Roboto:wght@500;700;900&family=Arimo:wght@400;700&display=swap" rel="stylesheet">
<style>
:root{
  --red:#9b1300;
  --red-bright:#c41a00;
  --ink:#1c1c1c;
  --muted:#8a8a8a;
  --soft:#f6f6f6;
  --dark:#111111;
  --white:#ffffff;
  --hero-a:#3f4a3a;
  --hero-b:#5a6342;
}
*{margin:0;padding:0;box-sizing:border-box}
html,body{width:1200px;height:4065px;overflow:hidden}
body{position:relative;background:var(--white);font-family:"Arimo",Arial,sans-serif;color:var(--ink)}
.abs{position:absolute}
.heading{font-family:"Roboto",Arial,sans-serif;font-weight:700;color:var(--ink);letter-spacing:-0.5px}
.eyebrow{font-family:"Arimo",Arial,sans-serif;font-size:12px;letter-spacing:2px;color:var(--red);text-transform:uppercase;font-weight:700}
.btn{position:absolute;display:flex;align-items:center;justify-content:center;background:var(--red);color:var(--white);font-size:11.5px;letter-spacing:1.3px;font-weight:700;text-transform:uppercase}
.para{font-size:13.5px;line-height:21px;color:#555}

/* header + hero */
.hero-photo{left:0;top:0;width:1200px;height:915px;background:linear-gradient(180deg,#3b4650 0%,#46513f 40%,#3d452f 70%,#4a4f3a 100%)}
.hero-shade{left:0;top:0;width:1200px;height:915px;background:rgba(20,22,24,.45)}
.brand{left:63px;top:36px;display:flex;align-items:center;gap:8px;color:var(--white);font-family:"Roboto",Arial,sans-serif;font-weight:700;font-size:19px;letter-spacing:1px}
.brand-mark{width:14px;height:14px;background:var(--red)}
.nav{left:384px;top:58px;display:flex;gap:38px;font-size:11.5px;letter-spacing:1px;color:var(--white)}
.nav .active{color:var(--red-bright)}
.hero-eyebrow{left:0;top:224px;width:1200px;text-align:center;color:var(--red-bright)}
.hero-title{left:0;top:262px;width:1200px;text-align:center;color:var(--white);font-size:78px;line-height:84px;font-weight:900}
.hero-text{left:0;top:552px;width:1200px;text-align:center;color:var(--white);font-size:16.5px;line-height:25px}

/* about */
.about-frame{left:629px;top:1008px;width:486px;height:290px;background:var(--red)}
.about-photo{left:590px;top:1066px;width:421px;height:270px;background:linear-gradient(160deg,#8b8f93,#4c4a45 55%,#6e6a62)}

/* trailers */
.trailers{left:0;top:1479px;width:1200px;height:705px;background:var(--soft)}
.card{position:absolute;top:213px;width:252px;height:386px;background:var(--white);box-shadow:0 2px 8px rgba(0,0,0,.08)}
.card-img{position:absolute;left:29px;top:20px;width:194px;height:66px;background:linear-gradient(180deg,#f3f3f3,#e6e6e6)}
.card-title{position:absolute;left:29px;top:126px;font-family:"Roboto",Arial,sans-serif;font-weight:700;font-size:16px}
.specs{position:absolute;left:29px;top:170px;list-style:none;font-size:13px;color:var(--muted)}
.specs li{display:flex;align-items:center;gap:16px;height:28px}
.specs li i{width:12px;height:12px;border-radius:50%;background:#c9c9c9;display:block}
.card .btn{left:29px;top:314px;width:138px;height:37px}

/* why choose */
.why-frame{left:73px;top:2347px;width:403px;height:342px;background:var(--red)}
.why-photo{left:137px;top:2288px;width:374px;height:361px;background:linear-gradient(180deg,#b9d2e6 0%,#7f9a5c 45%,#7b7a76 70%,#9a958c)}
.feature{position:absolute;width:260px}
.feature svg{position:absolute;left:0;top:0}
.feature h3{position:absolute;left:62px;top:-4px;font-family:"Roboto",Arial,sans-serif;font-weight:700;font-size:20px;line-height:22px;width:200px}
.feature p{position:absolute;left:62px;width:150px;font-size:13px;line-height:21px;color:var(--muted)}

/* testimonials */
.testi-bg{left:0;top:2820px;width:1200px;height:405px;background:linear-gradient(180deg,#3a4044,#2b3034 60%,#35393b)}
.testi-shade{left:0;top:2820px;width:1200px;height:405px;background:rgba(15,17,19,.5)}
.t-card{position:absolute;top:3110px;width:336px;height:249px;background:var(--white);box-shadow:0 2px 10px rgba(0,0,0,.1)}
.t-card p{position:absolute;left:28px;top:36px;width:285px;font-size:13px;line-height:21px;color:var(--muted)}
.stars{position:absolute;left:28px;top:128px;display:flex;gap:4px}
.avatar{position:absolute;left:28px;top:160px;width:58px;height:58px;border-radius:50%;background:linear-gradient(160deg,#9c8e80,#4e4740)}
.t-name{position:absolute;left:104px;top:168px;font-family:"Roboto",Arial,sans-serif;font-weight:700;font-size:15.5px}
.t-role{position:absolute;left:104px;top:190px;font-size:12px;color:#b3b3b3}

/* contact bar + footer */
.footer{left:0;top:3548px;width:1200px;height:517px;background:var(--dark)}
.contact-bar{left:19px;top:3493px;width:1162px;height:115px;background:var(--red);display:flex}
.contact-item{flex:1;display:flex;align-items:center;justify-content:center;gap:18px;color:var(--white);border-right:1px solid rgba(255,255,255,.15)}
.contact-item:last-child{border-right:none}
.contact-item b{display:block;font-family:"Roboto",Arial,sans-serif;font-size:22px;font-weight:700}
.contact-item span{font-size:12.5px}
.f-brand{left:87px;top:3705px;color:var(--white)}
.f-about{left:66px;top:3812px;width:290px;font-size:12.5px;line-height:20px;color:#d6d6d6}
.socials{left:66px;top:3885px;display:flex;gap:11px}
.socials i{display:block;width:34px;height:34px;background:#1e1e1e}
.f-col{color:var(--white)}
.f-col h4{font-family:"Roboto",Arial,sans-serif;font-weight:700;font-size:17px;margin-bottom:18px}
.f-col ul{list-style:none;font-size:12.5px;color:#e4e4e4}
.f-col li{height:29.5px;display:flex;align-items:center;gap:14px}
.f-col li::before{content:"›";color:var(--red-bright);font-size:17px}
.f-input{left:852px;top:3709px;width:280px;height:38px;background:var(--white);padding-left:12px;font-size:12px;color:#aaa;display:flex;align-items:center}
.copyright{left:0;top:4024px;width:1200px;text-align:center;font-size:12.5px;color:#e4e4e4}
.divider{left:0;top:3996px;width:1200px;height:1px;background:#222}
</style>
</head>
<body>

<!-- Header & hero -->
<div class="abs hero-photo" role="img" aria-label="Photo of a heavy haul truck pulling a lowboy trailer loaded with earthmoving equipment across flat Texas farmland"></div>
<div class="abs hero-shade"></div>
<svg class="abs" style="left:0;top:815px" width="1200" height="110" viewBox="0 0 1200 110">
  <polygon points="0,5 600,57 1200,5 1200,13 600,100 0,13" fill="#9b1300"/>
  <polygon points="0,13 600,100 1200,13 1200,110 0,110" fill="#ffffff"/>
</svg>

<div class="abs brand"><span class="brand-mark"></span>STEELBRAND</div>
<nav class="abs nav">
  <span class="active">HOME</span><span>ABOUT</span><span>TRAILERS</span><span>FINANCING</span><span>CONTACT</span>
</nav>
<div class="btn" style="left:990px;top:47px;width:136px;height:37px">Get Estimate</div>

<div class="abs eyebrow hero-eyebrow">Steelbrand</div>
<h1 class="abs heading hero-title">Quality Trailer<br>Manufacturer in<br>Texas</h1>
<p class="abs hero-text">We understand heavy haul trucking businesses succeed by safely hauling<br>the maximum payload weight that regulations will allow.</p>
<div class="btn" style="left:467px;top:621px;width:265px;height:37px">Request A Quote</div>

<!-- About -->
<div class="abs eyebrow" style="left:123px;top:1026px">About</div>
<h2 class="abs heading" style="left:123px;top:1048px;font-size:42px">Steelbrand</h2>
<p class="abs para" style="left:123px;top:1116px;width:400px">Lorem ipsum dolor sit amet, consectetur adipiscing elit. Doneca feugiat purus. Duis turpis nunc aliquam id nunc acconvallis dictum nisi. Curabitur vehicula tincidunt sapien velcac. Donec diam augue consequat sit amet metus acbibendum mattis massauis mollis ligula pretium consequat.</p>
<div class="btn" style="left:123px;top:1243px;width:177px;height:36px">Request A Quote</div>
<div class="abs about-frame"></div>
<div class="abs about-photo" role="img" aria-label="Photo of a black flatbed trailer deck with loading ramps parked on a residential street"></div>

<!-- Trailers -->
<section class="abs trailers">
  <div class="abs eyebrow" style="left:76px;top:104px">Browse Latest</div>
  <h2 class="abs heading" style="left:76px;top:126px;font-size:42px">Our Trailers</h2>
  <div class="btn" style="left:949px;top:137px;width:175px;height:37px">View All Trailers</div>

  <div class="card" style="left:57px">
    <div class="card-img" role="img" aria-label="Product photo of a black lowboy super haul trailer"></div>
    <div class="card-title">Super Haul</div>
    <ul class="specs"><li><i></i>P4000-8</li><li><i></i>Payload : 40 tons</li><li><i></i>Axle : 13</li><li><i></i>LB : 160000</li></ul>
    <div class="btn">View Details</div>
  </div>
  <div class="card" style="left:328px">
    <div class="card-img" role="img" aria-label="Product photo of a blue heavy haul flatbed trailer"></div>
    <div class="card-title">Heavy Haul</div>
    <ul class="specs"><li><i></i>P4000-8</li><li><i></i>Payload : 40 tons</li><li><i></i>Axle : 13</li><li><i></i>LB : 160000</li></ul>
    <div class="btn">View Details</div>
  </div>
  <div class="card" style="left:599px">
    <div class="card-img" role="img" aria-label="Product photo of a wooden deck special purpose trailer"></div>
    <div class="card-title">Special Purpose</div>
    <ul class="specs"><li><i></i>P4000-8</li><li><i></i>Payload : 40 tons</li><li><i></i>Axle : 13</li><li><i></i>LB : 160000</li></ul>
    <div class="btn">View Details</div>
  </div>
  <div class="card" style="left:870px">
    <div class="card-img" role="img" aria-label="Product photo of a red oilfield trailer"></div>
    <div class="card-title">Oilfield</div>
    <ul class="specs"><li><i></i>P4000-8</li><li><i></i>Payload : 40 tons</li><li><i></i>Axle : 13</li><li><i></i>LB : 160000</li></ul>
    <div class="btn">View Details</div>
  </div>
</section>

<!-- Why choose us -->
<div class="abs why-frame"></div>
<div class="abs why-photo" role="img" aria-label="Photo of a black gooseneck trailer with ramps parked on gravel beside trees"></div>
<div class="abs eyebrow" style="left:610px;top:2288px">Why Choose Us</div>
<h2 class="abs heading" style="left:610px;top:2310px;font-size:42px">Wide Range Of Trailers</h2>

<div class="feature" style="left:610px;top:2378px">
  <svg width="36" height="40" viewBox="0 0 36 40" fill="none" stroke="#9b1300" stroke-width="1.6"><circle cx="20" cy="12" r="7"/><path d="M20 8v8M2 28h8l8 3h8l8-6M2 36h10l10 2 12-8"/></svg>
  <h3>Competitive Pricing</h3><p style="top:30px">Lorem ipsum dolor sit amet consec tetur adipiscing elit pretium sollicitudin.</p>
</div>
<div class="feature" style="left:886px;top:2378px">
  <svg width="36" height="40" viewBox="0 0 36 40" fill="none" stroke="#9b1300" stroke-width="1.6"><circle cx="17" cy="20" r="14"/><path d="M10 20l6 6 14-16"/></svg>
  <h3>Quality Trailers</h3><p style="top:30px">Lorem ipsum dolor sit amet consec tetur adipiscing elit pretium sollicitudin.</p>
</div>
<div class="feature" style="left:610px;top:2541px">
  <svg width="38" height="40" viewBox="0 0 38 40" fill="none" stroke="#9b1300" stroke-width="1.6"><path d="M4 36L26 12M24 6a7 7 0 0 0 8 10l-3-3M6 6l28 28M4 8l4-4 6 6-4 4z"/></svg>
  <h3>Breakdown<br>Assistance</h3><p style="top:52px">Lorem ipsum dolor sit amet consec tetur adipiscing elit pretium sollicitudin.</p>
</div>
<div class="feature" style="left:886px;top:2541px">
  <svg width="38" height="40" viewBox="0 0 38 40" fill="none" stroke="#9b1300" stroke-width="1.6"><path d="M6 22a13 13 0 0 1 26 0"/><rect x="3" y="20" width="6" height="10" rx="2"/><rect x="29" y="20" width="6" height="10" rx="2"/><circle cx="19" cy="24" r="6"/><path d="M32 30c0 5-6 6-10 6"/></svg>
  <h3>24/7 Support</h3><p style="top:30px">Lorem ipsum dolor sit amet consec tetur adipiscing elit pretium sollicitudin.</p>
</div>

<!-- Testimonials -->
<div class="abs testi-bg" role="img" aria-label="Photo of a dark trailer parked outside a workshop yard"></div>
<div class="abs testi-shade"></div>
<div class="abs" style="left:0;top:2924px;width:1200px;text-align:center;color:#fff;font-size:12px;letter-spacing:2px;font-weight:700">TESTIMONIAL</div>
<h2 class="abs heading" style="left:0;top:2948px;width:1200px;text-align:center;color:#fff;font-size:42px">What Our Clients Say</h2>
<p class="abs" style="left:0;top:3013px;width:1200px;text-align:center;color:#fff;font-size:13.5px;line-height:22px">Lorem ipsum dolor sit amet, consectetur adipiscing elit, sed do eius tempor incididunt ut labore et<br>dolore magna aliqua. Adiqua minim veniam quis exercitation incididunt magna aliqua veniam quis.</p>

<div class="t-card" style="left:57px">
  <p>Lorem ipsum dolor sit amet, consectetur adip iscing elit, sed do eiusmod tempor incididunt ut labore et dolore magna aliqua.</p>
  <div class="stars"><svg width="96" height="16" viewBox="0 0 96 16" fill="#f5b400"><defs><polygon id="s" points="8,0 10,5.5 16,6 11.5,9.8 13,16 8,12.6 3,16 4.5,9.8 0,6 6,5.5"/></defs><use href="#s"/><use href="#s" x="20"/><use href="#s" x="40"/><use href="#s" x="60"/><use href="#s" x="80"/></svg></div>
  <div class="avatar" role="img" aria-label="Portrait of the client"></div>
  <div class="t-name">Marco Delvane</div><div class="t-role">Project Manager</div>
</div>
<div class="t-card" style="left:432px">
  <p>Lorem ipsum dolor sit amet, consectetur adip iscing elit, sed do eiusmod tempor incididunt ut labore et dolore magna aliqua.</p>
  <div class="stars"><svg width="96" height="16" viewBox="0 0 96 16" fill="#f5b400"><use href="#s"/><use href="#s" x="20"/><use href="#s" x="40"/><use href="#s" x="60"/><polygon points="88,0 90,5.5 96,6 91.5,9.8 93,16 88,12.6" fill="#f5b400"/></svg></div>
  <div class="avatar" role="img" aria-label="Portrait of the client" style="background:linear-gradient(160deg,#a7aaa7,#5a5d58)"></div>
  <div class="t-name">Lena Harwick</div><div class="t-role">Marketing Staff</div>
</div>
<div class="t-card" style="left:806px">
  <p>Lorem ipsum dolor sit amet, consectetur adip iscing elit, sed do eiusmod tempor incididunt ut labore et dolore magna aliqua.</p>
  <div class="stars"><svg width="96" height="16" viewBox="0 0 96 16" fill="#f5b400"><use href="#s"/><use href="#s" x="20"/><use href="#s" x="40"/><use href="#s" x="60"/></svg></div>
  <div class="avatar" role="img" aria-label="Portrait of the client" style="background:linear-gradient(160deg,#b0766a,#5a2a24)"></div>
  <div class="t-name">Owen Castrel</div><div class="t-role">IT Programmer</div>
</div>

<!-- Footer -->
<div class="abs footer"></div>
<div class="abs contact-bar">
  <div class="contact-item">
    <svg width="28" height="28" viewBox="0 0 24 24" fill="#fff"><path d="M6.6 10.8a15 15 0 0 0 6.6 6.6l2.2-2.2a1 1 0 0 1 1-.25 11.4 11.4 0 0 0 3.6.57 1 1 0 0 1 1 1V20a1 1 0 0 1-1 1A17 17 0 0 1 3 4a1 1 0 0 1 1-1h3.5a1 1 0 0 1 1 1c0 1.25.2 2.45.57 3.6a1 1 0 0 1-.25 1z"/></svg>
    <div><b>Call Us</b><span>+(1) 555-014-2290</span></div>
  </div>
  <div class="contact-item">
    <svg width="28" height="22" viewBox="0 0 28 22" fill="#fff"><path d="M0 2l14 10L28 2V0H0zM0 5v17h28V5L14 15z"/></svg>
    <div><b>Email Us</b><span>hello@steelbrand.example</span></div>
  </div>
  <div class="contact-item">
    <svg width="22" height="30" viewBox="0 0 22 30" fill="#fff"><path d="M11 0a11 11 0 0 0-11 11c0 8 11 19 11 19s11-11 11-19A11 11 0 0 0 11 0zm0 15a4 4 0 1 1 0-8 4 4 0 0 1 0 8z"/></svg>
    <div><b>Our Location</b><span>Ridgeway Rd 4410, Texas</span></div>
  </div>
  <div class="contact-item">
    <svg width="28" height="28" viewBox="0 0 28 28"><circle cx="14" cy="14" r="13" fill="#fff"/><path d="M14 7v8h6" stroke="#9b1300" stroke-width="2.5" fill="none"/></svg>
    <div><b>Work Hours</b><span>09:00 AM - 22:00 PM</span></div>
  </div>
</div>

<div class="abs brand f-brand" style="left:87px;top:3722px"><span class="brand-mark"></span>STEELBRAND</div>
<p class="abs f-about">Lorem ipsum dolor sit amet, consectetur adipiscing elit, sed do eiusmod tempor incididunt ut labore et dolore eiusmod tempor.</p>
<div class="abs socials" aria-label="Social media links"><i></i><i></i><i></i><i></i></div>

<div class="abs f-col" style="left:393px;top:3668px">
  <h4>Quick Links</h4>
  <ul><li>About</li><li>Trailers</li><li>Finance</li><li>FAQs</li><li>Contact</li></ul>
</div>
<div class="abs f-col" style="left:609px;top:3666px">
  <h4>Useful Links</h4>
  <ul><li>Privacy Policy</li><li>Terms and Conditions</li><li>Disclaimer</li><li>Support</li><li>FAQ</li></ul>
</div>
<div class="abs f-col" style="left:852px;top:3666px"><h4>Subscribe Our Newsletter</h4></div>
<div class="abs f-input">Your Email</div>
<div class="btn" style="left:852px;top:3769px;width:280px;height:38px">Subscribe</div>

<div class="abs divider"></div>
<div class="abs copyright">Copyright © 2023 Steelbrand. All rights reserved.</div>

</body>
</html>
```